Quiet Harbor Lane - The best guide in your pocket

Quiet Harbor Lane (آبیکوهستانها in Persian)

We need a new app design for a major update on Android, iOS and Windows Universal platforms.
Our company works on creating innovative apps and games on different platforms, this particular app is free for end users and provides location based services. Here is the abstract feature list:
• Nearest points around user (explore on map or find) including locations, events and skills
• Add points to our database (partners) plus comments and ratings
• Point owners can modify or complete their points data, provide sale events, services and …

Attachments:
Our service logo
The detailed descriptions of different sections (PDF documents)
Updates

Project Deadline Extended Reason: We want more designs :)Give us previews on Home and Map sections at least (more interesting if previews are provided for more sections) Added Saturday, January 7, 2017

Target Market(s)

Public

Industry/Entity Type

Android

Font styles to use
Serif
Sans Serif

Requirements
Must have
• Consider attached service logo & wireframe
• Designs for attached sections
• Fluent user experience
• Modern design
Nice to have
• Right to Left layouts
Should not have
• No alphabet in graphic assets

```html
<!DOCTYPE html>
<html lang="en">
<head>
<meta charset="utf-8">
<title>آبیکوهستانها — Home</title>
<link href="https://fonts.googleapis.com/css2?family=Source+Sans+3:wght@300;400;600;700&family=Vazirmatn:wght@500&display=swap" rel="stylesheet">
<style>
  :root {
    --teal: #7cc8c0;
    --teal-deep: #3f8f8a;
    --slate: #34505a;
    --slate-dark: #2d4650;
    --ink: #222222;
    --muted: #8a8a8a;
    --line: #e4e4e4;
    --page: #f2f3f4;
    --white: #ffffff;
    --map-land: #e3e6e4;
    --map-water: #a9cbd6;
  }
  * { box-sizing: border-box; margin: 0; padding: 0; }
  html, body { width: 1000px; height: 1200px; overflow: hidden; }
  body { background: var(--page); font-family: "Source Sans 3", "Helvetica Neue", sans-serif; color: var(--ink); }

  .screen { position: absolute; left: 162px; top: 0; width: 675px; height: 1200px; background: var(--white); overflow: hidden; }

  /* status + header */
  .app-bar { position: absolute; left: 0; top: 0; width: 100%; height: 137px; background: var(--teal); }
  .status-bar { position: absolute; top: 0; left: 0; width: 100%; height: 45px; display: flex; align-items: center; justify-content: space-between; padding: 0 14px; font-size: 21px; font-weight: 600; color: #111; }
  .status-left, .status-right { display: flex; align-items: center; gap: 6px; }
  .signal { display: flex; gap: 3px; }
  .signal i { width: 10px; height: 10px; border-radius: 50%; background: #111; display: block; }
  .signal i.off { background: transparent; border: 1.5px solid #111; }
  .battery { width: 40px; height: 16px; background: #111; border-radius: 3px; position: relative; }
  .battery::after { content: ""; position: absolute; right: -4px; top: 5px; width: 3px; height: 6px; background: #111; border-radius: 0 2px 2px 0; }
  .menu-button { position: absolute; left: 28px; top: 82px; }
  .brand { position: absolute; left: 0; right: 0; top: 68px; text-align: center; font-family: "Vazirmatn", sans-serif; font-weight: 500; font-size: 34px; color: var(--teal-deep); direction: rtl; }
  .globe-button { position: absolute; right: 26px; top: 72px; }

  /* map */
  .map { position: absolute; left: 0; top: 137px; width: 100%; height: 562px; background: linear-gradient(160deg, var(--map-water) 0%, var(--map-water) 28%, var(--map-land) 42%, var(--map-land) 100%); }
  .search-bar { position: absolute; left: 12px; top: 15px; width: 648px; height: 60px; background: var(--white); box-shadow: 0 1px 4px rgba(0,0,0,.12); display: flex; align-items: center; padding-left: 24px; font-size: 22px; color: #9a9a9a; gap: 16px; }
  .filter-button { position: absolute; right: 12px; top: 8px; width: 44px; height: 44px; background: var(--slate); border-radius: 3px; display: flex; align-items: center; justify-content: center; }
  .categories { position: absolute; left: 436px; top: 78px; width: 205px; height: 269px; background: var(--white); box-shadow: 0 2px 6px rgba(0,0,0,.12); padding: 18px 0 0 18px; font-size: 15px; }
  .categories::before { content: ""; position: absolute; right: 20px; top: -8px; border: 8px solid transparent; border-top: 0; border-bottom-color: var(--white); }
  .categories-title { display: flex; align-items: center; gap: 8px; color: #333; font-size: 14px; margin-bottom: 14px; }
  .category { color: var(--muted); height: 33px; }
  .category.active { color: var(--ink); }
  .category span { color: var(--teal); }
  .scroll-track { position: absolute; right: 14px; top: 20px; width: 3px; height: 240px; background: #eee; }
  .scroll-thumb { position: absolute; right: 14px; top: 20px; width: 3px; height: 155px; background: var(--slate); }

  .place-tooltip { position: absolute; left: 17px; top: 281px; width: 215px; height: 95px; background: var(--teal); border-bottom: 4px solid var(--slate); color: var(--white); text-align: center; padding-top: 18px; }
  .place-tooltip strong { display: block; font-size: 19px; font-weight: 700; }
  .place-tooltip small { display: block; font-size: 14px; margin-top: 8px; }
  .place-tooltip::after { content: ""; position: absolute; left: 107px; bottom: -12px; border: 8px solid transparent; border-top-color: var(--slate); }
  .pin { position: absolute; }
  .user-dot { position: absolute; left: 248px; top: 447px; width: 60px; height: 60px; border-radius: 50%; background: rgba(124,200,192,.25); display: flex; align-items: center; justify-content: center; }
  .user-dot i { width: 26px; height: 26px; border-radius: 50%; background: var(--teal); border: 3px solid var(--white); display: block; }

  /* tabs */
  .tabs { position: absolute; left: 0; top: 699px; width: 100%; height: 99px; display: flex; background: var(--white); }
  .tab { flex: 1; display: flex; align-items: center; justify-content: center; font-size: 18px; font-weight: 700; letter-spacing: 1.5px; border-right: 1px solid var(--line); position: relative; }
  .tab:last-child { border-right: 0; }
  .tab.active::after { content: ""; position: absolute; left: 0; right: 0; bottom: 0; height: 6px; background: var(--teal); }

  /* list */
  .place-list { position: absolute; left: 0; top: 798px; width: 100%; height: 402px; background: var(--slate); padding: 11px; display: flex; flex-direction: column; gap: 12px; }
  .place-card { height: 182px; background: var(--white); position: relative; }
  .place-photo { position: absolute; left: 25px; top: 27px; width: 127px; height: 127px; background: linear-gradient(180deg, #5a2e14 0%, #a4582a 45%, #3a1e10 100%); }
  .place-name { position: absolute; left: 178px; top: 50px; font-size: 32px; font-weight: 400; }
  .place-address { position: absolute; left: 178px; top: 100px; font-size: 22px; font-weight: 300; color: #666; }
  .place-type { position: absolute; right: 25px; top: 26px; font-size: 19px; color: var(--teal); letter-spacing: .5px; }
  .place-distance { position: absolute; right: 25px; top: 54px; font-size: 36px; font-weight: 400; }
  .visitors { position: absolute; right: 22px; top: 112px; display: flex; gap: 6px; }
  .visitor { width: 48px; height: 48px; border-radius: 50%; background: linear-gradient(135deg, #6b4a30, #c89a72); }
  .visitor-more { width: 48px; height: 48px; border-radius: 50%; background: #e6e6e6; color: #888; font-size: 18px; display: flex; align-items: center; justify-content: center; }
</style>
</head>
<body>
<main class="screen">
  <header class="app-bar">
    <div class="status-bar">
      <div class="status-left">
        <span class="signal"><i></i><i></i><i></i><i class="off"></i><i class="off"></i></span>
        <span>NOVA</span>
        <svg width="20" height="16" viewBox="0 0 20 16"><path d="M2 6a12 12 0 0 1 16 0M5 9a7 7 0 0 1 10 0M8 12a3 3 0 0 1 4 0" fill="none" stroke="#111" stroke-width="2.2" stroke-linecap="round"/></svg>
      </div>
      <div>4:21 PM</div>
      <div class="status-right">
        <svg width="12" height="18" viewBox="0 0 12 18"><path d="M1 5l9 8-4 4V1l4 4-9 8" fill="none" stroke="#333" stroke-width="1.4"/></svg>
        <span>100%</span>
        <span class="battery"></span>
      </div>
    </div>
    <svg class="menu-button" width="34" height="20" viewBox="0 0 34 20"><path d="M0 2h34M0 10h34M0 18h34" stroke="#fff" stroke-width="3"/></svg>
    <div class="brand">آبیکوهستانها</div>
    <svg class="globe-button" width="40" height="40" viewBox="0 0 40 40"><circle cx="20" cy="20" r="18" fill="#fff"/><path d="M10 10c6 2 8 6 5 10s2 8 0 14M24 4c-3 5 2 8 7 8s5 8 2 12" fill="none" stroke="var(--teal)" stroke-width="3"/></svg>
  </header>

  <section class="map" role="img" aria-label="Street map of the harbour district around the user's position">
    <div class="search-bar">
      <svg width="20" height="20" viewBox="0 0 20 20"><circle cx="11" cy="8" r="6" fill="none" stroke="#aaa" stroke-width="1.8"/><path d="M7 12l-5 6" stroke="#aaa" stroke-width="1.8"/></svg>
      <span>Search</span>
      <div class="filter-button">
        <svg width="26" height="26" viewBox="0 0 26 26" fill="none" stroke="#fff" stroke-width="2"><path d="M5 2v22M13 2v22M21 2v22"/><circle cx="5" cy="17" r="3" fill="var(--slate)"/><circle cx="13" cy="8" r="3" fill="var(--slate)"/><circle cx="21" cy="15" r="3" fill="var(--slate)"/></svg>
      </div>
    </div>

    <div class="categories">
      <div class="categories-title">
        <svg width="12" height="12" viewBox="0 0 12 12"><path d="M1 1h6v5H1zM3 10h1M6 10h1M9 10h1" fill="none" stroke="#555" stroke-width="1.3"/></svg>
        Catégories
      </div>
      <div class="category">Karaoke <span>(17)</span></div>
      <div class="category">Restaurant <span>(9)</span></div>
      <div class="category active">Club <span>(72)</span></div>
      <div class="category">Pub <span>(17)</span></div>
      <div class="category">Hotel <span>(17)</span></div>
      <div class="category">Beach <span>(17)</span></div>
      <div class="scroll-track"></div>
      <div class="scroll-thumb"></div>
    </div>

    <div class="place-tooltip"><strong>Lantern Room</strong><small>12 Willow Bend</small></div>

    <svg class="pin" style="left:318px;top:291px" width="44" height="58" viewBox="0 0 44 58"><ellipse cx="22" cy="54" rx="10" ry="3" fill="rgba(0,0,0,.2)"/><path d="M22 52C10 36 2 28 2 20a20 20 0 0 1 40 0c0 8-8 16-20 32z" fill="var(--slate)" stroke="var(--teal)" stroke-width="3"/><path d="M17 11v18M14 11v6h6v-6M26 11c3 0 3 8 0 8v10" stroke="#fff" stroke-width="2" fill="none"/></svg>
    <svg class="pin" style="left:102px;top:400px" width="44" height="58" viewBox="0 0 44 58"><ellipse cx="22" cy="54" rx="10" ry="3" fill="rgba(0,0,0,.2)"/><path d="M22 52C10 36 2 28 2 20a20 20 0 0 1 40 0c0 8-8 16-20 32z" fill="var(--slate)" stroke="var(--teal)" stroke-width="3"/><rect x="13" y="12" width="18" height="16" fill="none" stroke="#fff" stroke-width="2"/><path d="M17 17h2M21 17h2M25 17h2M17 22h2M21 22h2M25 22h2" stroke="#fff" stroke-width="2"/></svg>
    <svg class="pin" style="left:558px;top:442px" width="44" height="58" viewBox="0 0 44 58"><ellipse cx="22" cy="54" rx="10" ry="3" fill="rgba(0,0,0,.2)"/><path d="M22 52C10 36 2 28 2 20a20 20 0 0 1 40 0c0 8-8 16-20 32z" fill="var(--slate)" stroke="var(--teal)" stroke-width="3"/><path d="M15 12h11v17H15zM26 16h4v8h-4" fill="none" stroke="#fff" stroke-width="2"/></svg>
    <div class="user-dot"><i></i></div>
  </section>

  <nav class="tabs">
    <div class="tab active">MOST POPULAR</div>
    <div class="tab">NEAR ME</div>
    <div class="tab">NEWEST PLACES</div>
  </nav>

  <section class="place-list">
    <article class="place-card">
      <div class="place-photo" role="img" aria-label="Photo of the bar interior"></div>
      <h2 class="place-name">Lantern Room</h2>
      <p class="place-address">12 Willow Bend</p>
      <p class="place-type">CLUB</p>
      <p class="place-distance">0.6 mi</p>
      <div class="visitors">
        <div class="visitor" role="img" aria-label="Visitor avatar"></div>
        <div class="visitor" role="img" aria-label="Visitor avatar"></div>
        <div class="visitor" role="img" aria-label="Visitor avatar"></div>
        <div class="visitor-more">+2</div>
      </div>
    </article>
    <article class="place-card">
      <div class="place-photo" role="img" aria-label="Photo of the bar interior"></div>
      <h2 class="place-name">Lantern Room</h2>
      <p class="place-address">12 Willow Bend</p>
      <p class="place-type">CLUB</p>
      <p class="place-distance">0.6 mi</p>
      <div class="visitors">
        <div class="visitor" role="img" aria-label="Visitor avatar"></div>
        <div class="visitor" role="img" aria-label="Visitor avatar"></div>
        <div class="visitor" role="img" aria-label="Visitor avatar"></div>
        <div class="visitor-more">+2</div>
      </div>
    </article>
  </section>
</main>
</body>
</html>
```